Wedding Day Custom Wine Label - Tasmanian (Tamar Valley) wine

I am looking for a custom design that will be put on a wine label to commemorate a very good friend's wedding day.

We will need to be able to take the design and print it on to sticker labels that we can put on to wine bottles.

The bride and groom have asked for a simplistic label design (see example image attached). We need two labels. One for "Pinot Noir" wine and the other for "Chardonnay" wine. We would like the label to say:

The Hartwell's
Pinot Noir
2023
Tamar Valley

and for for the other wine variety:

The Hartwell's
Chardonnay
2023
Tamar Valley

smaller text below to say:

13.5% ALC/VOL 750ML
MEGAN & LIAM - 31.10.2024

I am happy to consider other variations - the bride & groom would prefer something minimalistic. Elegant and classy.

Target Market(s)

the bride & groom

Requirements
Must have
• Wedding date (31.10.2024). Wine type (Pinot Noir or Chardonnay).
Should not have
• images not essential

```html
<!DOCTYPE html>
<html lang="en">
<head>
<meta charset="utf-8">
<title>The Hartwell's – Wedding Wine Labels</title>
<link href="https://fonts.googleapis.com/css2?family=Fredoka:wght@500;600&family=Kaushan+Script&display=swap" rel="stylesheet">
<style>
  :root {
    --page-bg: #efefef;
    --label-bg: #f7f4e6;
    --ink: #111111;
    --shadow: rgba(0, 0, 0, 0.12);
  }
  * { margin: 0; padding: 0; box-sizing: border-box; }
  html, body {
    width: 1200px;
    height: 800px;
    overflow: hidden;
    background: var(--page-bg);
  }
  .canvas {
    position: relative;
    width: 1200px;
    height: 800px;
  }
  .wine-label {
    position: absolute;
    top: 153px;
    width: 380px;
    height: 493px;
    background: var(--label-bg);
    box-shadow: 0 6px 18px var(--shadow);
    color: var(--ink);
    font-family: "Fredoka", sans-serif;
    text-transform: uppercase;
    text-align: center;
  }
  .wine-label--pinot { left: 170px; }
  .wine-label--chardonnay { left: 650px; }

  .couple {
    position: absolute;
    top: 86px;
    left: 0;
    right: 0;
    font-weight: 600;
    font-size: 18px;
    letter-spacing: 0.2em;
    line-height: 1;
  }
  .wedding-date {
    position: absolute;
    top: 111px;
    left: 0;
    right: 0;
    font-weight: 600;
    font-size: 11px;
    letter-spacing: 0.14em;
    line-height: 1;
  }
  .family-name {
    position: absolute;
    top: 170px;
    left: 0;
    right: 0;
    font-family: "Kaushan Script", cursive;
    font-size: 58px;
    line-height: 1;
    text-transform: none;
    transform: rotate(-6deg);
    letter-spacing: -0.01em;
  }
  .variety {
    position: absolute;
    top: 284px;
    left: 0;
    right: 0;
    font-weight: 600;
    font-size: 25px;
    letter-spacing: 0.16em;
    line-height: 1;
  }
  .vintage {
    position: absolute;
    top: 311px;
    left: 0;
    right: 0;
    font-weight: 600;
    font-size: 25px;
    letter-spacing: 0.16em;
    line-height: 1;
  }
  .region {
    position: absolute;
    top: 340px;
    left: 0;
    right: 0;
    font-weight: 600;
    font-size: 16px;
    letter-spacing: 0.22em;
    line-height: 1;
  }
  .spec {
    position: absolute;
    top: 428px;
    font-weight: 600;
    font-size: 12px;
    letter-spacing: 0.14em;
    line-height: 1;
  }
  .spec--abv { left: 60px; }
  .spec--volume { right: 60px; }
</style>
</head>
<body>
<main class="canvas">
  <section class="wine-label wine-label--pinot">
    <p class="couple">Megan &amp; Liam</p>
    <p class="wedding-date">31-10-2024</p>
    <h1 class="family-name">The Hartwell's</h1>
    <p class="variety">Pinot Noir</p>
    <p class="vintage">2023</p>
    <p class="region">Tamar Valley</p>
    <p class="spec spec--abv">13.5% ALC/VOL</p>
    <p class="spec spec--volume">750ML</p>
  </section>

  <section class="wine-label wine-label--chardonnay">
    <p class="couple">Megan &amp; Liam</p>
    <p class="wedding-date">31-10-2024</p>
    <h2 class="family-name">The Hartwell's</h2>
    <p class="variety">Chardonnay</p>
    <p class="vintage">2023</p>
    <p class="region">Tamar Valley</p>
    <p class="spec spec--abv">13.5% ALC/VOL</p>
    <p class="spec spec--volume">750ML</p>
  </section>
</main>
</body>
</html>
```